Business card for femtech company

Nothing too elaborate but elegant and geared towards the mother and baby market. Prefer full-bleed with logo (attached) rear.

```html
<!DOCTYPE html>
<html lang="en">
<head>
<meta charset="utf-8">
<title>Nestwell Business Card</title>
<link href="https://fonts.googleapis.com/css2?family=Poppins:wght@400;500&display=swap" rel="stylesheet">
<style>
  :root {
    --teal: #5ac4b9;
    --teal-deep: #3f9a90;
    --grey: #acacac;
    --ink: #2b2b2b;
    --muted: #9a9a9a;
    --paper: #ffffff;
    --backdrop: #c4c4c4;
  }
  * { box-sizing: border-box; margin: 0; padding: 0; }
  html, body {
    width: 1200px; height: 800px; overflow: hidden;
    background: var(--backdrop);
    font-family: "Poppins", sans-serif;
  }
  .sheet {
    width: 1200px; height: 800px;
    display: flex; align-items: center; justify-content: center; gap: 40px;
  }
  .card {
    position: relative;
    width: 540px; height: 308px;
    border-radius: 18px;
    overflow: hidden;
  }
  .card-front { background: var(--paper); }
  .card-back { background: var(--teal); display: flex; align-items: center; justify-content: center; }

  .identity { position: absolute; left: 36px; top: 40px; }
  .identity-name { font-size: 26px; font-weight: 500; color: var(--muted); line-height: 1.1; }
  .identity-name .surname { color: var(--teal); }
  .identity-role { font-size: 14px; color: var(--ink); margin-top: 2px; }

  .contact-band {
    position: absolute; left: 0; top: 122px;
    width: 330px; height: 78px;
    background: var(--teal);
    padding: 8px 0 0 36px;
    color: var(--paper);
  }
  .contact-line { display: flex; align-items: center; gap: 8px; font-size: 13.5px; line-height: 21px; }
  .contact-line svg { width: 13px; height: 13px; flex: none; }

  .accent-band {
    position: absolute; right: 0; top: 122px;
    width: 70px; height: 78px;
    background: var(--grey);
  }
  .brand-slot {
    position: absolute; left: 330px; top: 122px;
    width: 140px; height: 78px;
    display: flex; align-items: center; justify-content: center; gap: 6px;
  }
  .brand-dot { width: 12px; height: 12px; border-radius: 50%; background: var(--teal); }
  .brand-name { font-size: 22px; font-weight: 500; color: var(--teal); }

  .address {
    position: absolute; left: 36px; top: 228px;
    font-size: 15px; color: var(--ink); line-height: 22px;
  }

  .back-brand { display: flex; align-items: center; gap: 16px; }
  .back-brand .brand-dot { width: 40px; height: 40px; background: var(--teal-deep); }
  .back-brand .brand-name { font-size: 48px; color: var(--teal-deep); }
</style>
</head>
<body>
<main class="sheet">
  <section class="card card-front" aria-label="Business card front">
    <div class="identity">
      <p class="identity-name">Daniel <span class="surname">Hart</span></p>
      <p class="identity-role">Managing Director</p>
    </div>

    <div class="contact-band">
      <p class="contact-line">
        <svg viewBox="0 0 16 16" aria-hidden="true"><path fill="currentColor" d="M3.6 1.5l2.2 2.6-1.2 1.8c.9 2 2.5 3.6 4.5 4.5l1.8-1.2 2.6 2.2-1.3 2.4C7 13.6 2.4 9 1.2 2.8z"/></svg>
        055-210 384 617
      </p>
      <p class="contact-line">
        <svg viewBox="0 0 16 16" aria-hidden="true"><rect x="1" y="3" width="14" height="10" fill="currentColor"/><path d="M1 3l7 6 7-6" fill="none" stroke="#5ac4b9" stroke-width="1.4"/></svg>
        hello@nestwell.com
      </p>
      <p class="contact-line">
        <svg viewBox="0 0 16 16" aria-hidden="true"><circle cx="8" cy="8" r="7" fill="currentColor"/><path d="M1 8h14M8 1v14M3 4.5h10M3 11.5h10" stroke="#5ac4b9" stroke-width="1"/><ellipse cx="8" cy="8" rx="3" ry="7" fill="none" stroke="#5ac4b9" stroke-width="1"/></svg>
        www.nestwell.com
      </p>
    </div>

    <div class="brand-slot">
      <span class="brand-dot"></span>
      <span class="brand-name">Nestwell</span>
    </div>
    <div class="accent-band"></div>

    <address class="address" style="font-style:normal">
      18 Meadow Lane, Suite 4<br>
      20931, Portland
    </address>
  </section>

  <section class="card card-back" aria-label="Business card back">
    <div class="back-brand">
      <span class="brand-dot"></span>
      <span class="brand-name">Nestwell</span>
    </div>
  </section>
</main>
</body>
</html>
```